Flyer/email in the style of the front page of a newspaper

I would like a flyer designing that i can primt and also insert into an email. I would like the following headings on the page: Free boards/Free re-brand. Independent family business. Orders completed in 2 working days. Established in 1997. Fitters with 15 years experience

Target Market(s)

business to business

Industry/Entity Type

Real Estate Agent

Requirements
Must have
• newspaper front page

```html
<!DOCTYPE html>
<html lang="en">
<head>
<meta charset="utf-8">
<title>Truesign – Free Boards / Free Re-Brand</title>
<link rel="stylesheet" href="https://fonts.googleapis.com/css2?family=League+Gothic&family=Merriweather:wght@700&family=Montserrat:wght@800&family=Open+Sans:wght@600&family=Oswald:wght@500&display=swap">
<style>
  :root {
    --backdrop: #ececec;
    --paper: #ffffff;
    --ink: #231f20;
    --navy: #1d2358;
    --red: #c8102e;
    --rule: #9a9a9b;
    --panel: #e6e6e7;
    --panel-edge: #a9a9aa;
    --icon-grey: #8c8c8e;
  }
  html, body { margin: 0; padding: 0; overflow: hidden; }
  body { width: 1184px; height: 1200px; background: var(--backdrop); position: relative; }
  .flyer {
    position: absolute; left: 184px; top: 66px; width: 805px; height: 1040px;
    background: var(--paper); box-shadow: 0 2px 6px rgba(0,0,0,.25);
  }
  .flyer > * { position: absolute; }
  .brand {
    left: 0; right: 0; top: 50px; text-align: center; white-space: nowrap;
    font: 800 72px/1 "Montserrat", sans-serif; color: var(--navy); letter-spacing: -1px;
  }
  .brand::before {
    content: ""; display: inline-block; width: 22px; height: 22px; background: var(--navy);
    margin-right: 14px; vertical-align: 10px;
  }
  .headline {
    left: 0; right: 0; top: 176px; margin: 0; text-align: center; white-space: nowrap;
    font: 400 88px/1 "League Gothic", sans-serif; color: var(--ink); letter-spacing: 0.5px;
  }
  .kicker { margin: 0; font: 700 21px/1.38 "Merriweather", serif; color: var(--ink); }
  .kicker--left { left: 38px; top: 284px; width: 180px; }
  .kicker--right { left: 647px; top: 277px; width: 130px; font-size: 15.5px; }
  .kicker--wide { left: 40px; top: 786px; font-size: 21px; white-space: nowrap; }
  .copy {
    background: repeating-linear-gradient(to bottom, var(--rule) 0 6px, transparent 6px 15.6px);
  }
  .copy--left { left: 40px; top: 359px; width: 172px; height: 392px; }
  .copy--mid-a { left: 242px; top: 560px; width: 172px; height: 192px; }
  .copy--mid-b { left: 444px; top: 560px; width: 172px; height: 192px; }
  .copy--right { left: 647px; top: 358px; width: 118px; height: 248px; }
  .copy--right-end { left: 647px; top: 728px; width: 118px; height: 22px; }
  .copy--full { left: 40px; top: 827px; width: 558px; height: 38px; }
  .copy--half-a { left: 40px; top: 883px; width: 267px; height: 54px; }
  .copy--half-b { left: 330px; top: 883px; width: 268px; height: 54px; }
  .photo--lead {
    left: 240px; top: 275px; width: 381px; height: 260px;
    background: linear-gradient(90deg, #7c4b3f 0 12%, #cfee3b 12% 24%, #1f6e5d 24% 58%, #cfee3b 58% 69%, #c09178 69% 100%);
  }
  .photo--side {
    left: 647px; top: 614px; width: 118px; height: 106px;
    background: linear-gradient(160deg, #d8e6f2 0%, #7fa8cf 35%, #1c2a3c 60%, #2c3e50 100%);
  }
  .column-rule { left: 631px; top: 276px; width: 1px; height: 475px; background: var(--ink); }
  .section-rule { left: 40px; top: 773px; width: 725px; height: 1px; background: var(--rule); }
  .call-box {
    left: 636px; top: 804px; width: 128px; height: 131px; box-sizing: border-box;
    background: var(--panel); border: 1px solid var(--panel-edge); text-align: center;
  }
  .call-box svg { display: block; margin: 20px auto 0; }
  .call-box .number {
    display: block; margin-top: 14px; white-space: nowrap;
    font: 500 20px/1 "Oswald", sans-serif; color: var(--navy); letter-spacing: -.5px;
  }
  .contact-bar {
    left: 40px; top: 971px; width: 735px; height: 35px; box-sizing: border-box;
    border: 1px solid var(--ink); display: flex; align-items: center;
    font: 600 13px/1 "Open Sans", sans-serif; color: #111; white-space: nowrap;
  }
  .contact-bar .label { color: var(--navy); }
  .contact-bar .item { display: flex; align-items: center; gap: 8px; }
  .contact-bar svg { flex: none; }
</style>
</head>
<body>
  <article class="flyer">
    <div class="brand">Truesign</div>
    <h1 class="headline">FREE BOARDS/FREE RE-BRAND</h1>

    <h2 class="kicker kicker--left">Independent family business.</h2>
    <div class="copy copy--left"></div>

    <div class="photo photo--lead" role="img" aria-label="Close-up of a lime-green For Sale board with a dark green panel in front of a brick house"></div>
    <div class="copy copy--mid-a"></div>
    <div class="copy copy--mid-b"></div>

    <div class="column-rule"></div>
    <h2 class="kicker kicker--right">Orders completed in 2 working days.</h2>
    <div class="copy copy--right"></div>
    <div class="photo photo--side" role="img" aria-label="Navy To Let sign hanging from a post against a blue sky"></div>
    <div class="copy copy--right-end"></div>

    <div class="section-rule"></div>
    <h2 class="kicker kicker--wide">Established in 1997. Fitters with 15 years experience</h2>
    <div class="copy copy--full"></div>
    <div class="copy copy--half-a"></div>
    <div class="copy copy--half-b"></div>

    <div class="call-box">
      <svg width="34" height="56" viewBox="0 0 34 56" aria-hidden="true">
        <rect x="6" y="0" width="5" height="10" rx="2" fill="var(--icon-grey)"/>
        <rect x="0" y="8" width="34" height="48" rx="9" fill="var(--icon-grey)"/>
        <rect x="6" y="16" width="22" height="14" rx="2" fill="var(--panel)"/>
        <circle cx="17" cy="44" r="3" fill="var(--panel)"/>
      </svg>
      <span class="number">0300 555 0142</span>
    </div>

    <footer class="contact-bar">
      <span class="label" style="margin-left:26px">Contact Us</span>
      <span class="item" style="margin-left:24px">
        <svg width="19" height="14" viewBox="0 0 19 14" aria-hidden="true"><rect x="1" y="1" width="17" height="12" fill="none" stroke="var(--red)" stroke-width="1.6"/><path d="M1 1 L9.5 8 L18 1 M1 13 L7 7 M18 13 L12 7" fill="none" stroke="var(--red)" stroke-width="1.4"/></svg>
        icon_mail info@truesign.co.uk
      </span>
      <span class="label" style="margin-left:62px">Learn more</span>
      <span class="item" style="margin-left:22px">
        <svg width="18" height="18" viewBox="0 0 18 18" aria-hidden="true"><circle cx="9" cy="9" r="7.5" fill="none" stroke="var(--red)" stroke-width="1.6"/><path d="M1.5 9 H16.5 M9 1.5 C5 5 5 13 9 16.5 M9 1.5 C13 5 13 13 9 16.5" fill="none" stroke="var(--red)" stroke-width="1.3"/></svg>
        www.truesign.co.uk
      </span>
    </footer>
  </article>
</body>
</html>
```